Plumbing Contractor Website Design

We are working with a Plumbing contractor in CA called KT Plumbline.

Some sites to use for content/competitors and inspiration:

https://www.pipevalex.com
https://www.drainmoss.com
https://quillbark.example/web/contractor/ (lots of contractor website designs we've approved and continue to show clients)

Thank you for taking the time to consider designing a website for us. We are web developers based in Stockton, CA, USA. Most of our projects go through the same process. Understanding this process may help you win a project with us. We custom-code all of our websites in-house. We don’t have any requirements as to what tools you use for your design, but we prefer Figma files. For any design that we label as four-stars, we send it to the client for review. The client picks the final design they want us to use. Once we complete this process, we will continue to show additional clients all the four-star sites and purchase them later. Your designs will have multiple chances to sell. For better chances of success, we ask that you follow these guidelines.

IMAGES:
If you use any images or icons in the design, we ask that you have a link to the asset so we can purchase the image/icon. Most of the designs we submit do not have the customer’s images on them unless they have some great images. Be creative; show us the feeling you are trying to portray with your image choices. Use any royalty-free site you choose. We subscribe to Adobe and mainly use their images, but we can purchase images outside of Adobe.

PLEASE NOTE: we will not submit designs to clients with watermarks on the images.

FONTS:
We ask that you identify the fonts used in the design. This can be done in a message if you want. We typically use Google Fonts and Adobe Fonts.

CONTENT:
We're always open to different content and ideas. We often submit designs with stock images so the client can see our vision. We typically take pictures after the website launch to use their images with our vision. Lorem Ipsum is fine for paragraphs, but we ask that you write the headers in correct English. We want to be able to show the vision and identify the sections of the website.

INSPIRATION:
We typically add a couple of links in the brief of websites we like to help you get started in your design.

REVISIONS:
We do not often ask for revisions of the designs unless we see something in the design that may not appeal to the client. If there are slight changes that we want to make, we do that in the development process.

FEEDBACK:
We rarely give feedback on designs during the design process. We are working on many website projects and do not have the time to provide feedback. We usually respond if your request is well thought out and asks specific questions, but a note asking “feedback, please” usually goes unanswered

```html
<!DOCTYPE html>
<html lang="en">
<head>
<meta charset="utf-8">
<title>KT Plumbline — Expert Plumbing Solutions in California</title>
<link href="https://fonts.googleapis.com/css2?family=Lexend:wght@400;500&family=Poppins:wght@400;500&display=swap" rel="stylesheet">
<style>
:root{
  --blue:#0b5b8e;
  --blue-dark:#064a76;
  --ink:#111;
  --text:#2b2b2b;
  --white:#fff;
  --line:#d9d9d9;
}
*{margin:0;padding:0;box-sizing:border-box}
h1,h2,h3{font-weight:400}
html,body{width:1200px;height:3600px;overflow:hidden;background:var(--white)}
body{position:relative;font-family:"Poppins",sans-serif;color:var(--text)}
.abs{position:absolute}
.btn{position:absolute;display:flex;align-items:center;justify-content:center;font-family:"Lexend",sans-serif;font-size:13px;font-weight:500;letter-spacing:.3px;clip-path:polygon(6px 0,100% 0,calc(100% - 6px) 100%,0 100%)}
.btn-blue{background:var(--blue);color:var(--white)}
.btn-white{background:var(--white);color:var(--blue)}
.photo{position:absolute}
.call{left:112px;top:31px;font-size:13px;color:var(--blue);display:flex;align-items:center;gap:10px}
.nav-band{left:105px;top:95px;width:985px;height:38px;background:var(--blue-dark)}
.nav a{position:absolute;top:95px;height:38px;line-height:38px;color:var(--white);font-size:12.5px;text-decoration:none;font-family:"Lexend",sans-serif}
.nav a.active{background:#2d2d2d;padding:0 12px}
.logo-disc{left:527px;top:6px;width:146px;height:140px;border-radius:50%;background:var(--white)}
.logo-name{font-family:"Lexend",sans-serif;font-weight:500;color:var(--blue);text-align:center}
.hero-title{left:545px;top:200px;font-size:34px;line-height:48px;color:var(--white);font-family:"Lexend",sans-serif;font-weight:400}
.hero-text{left:545px;top:308px;width:560px;font-size:15.5px;line-height:36px;color:var(--white)}
.sec-title{font-family:"Lexend",sans-serif;font-weight:400;font-size:30px;display:flex;align-items:center;gap:14px}
.sec-title .accent{color:var(--blue)}
.para{font-size:15.5px;line-height:34px;color:var(--text)}
.card{position:absolute;top:1285px;width:303px;height:352px;border:1.5px dashed rgba(255,255,255,.75);border-radius:0 0 8px 60px}
.card .img{position:absolute;left:5px;top:5px;right:5px;height:190px;border-radius:4px}
.card h3{position:absolute;top:220px;width:100%;text-align:center;font-family:"Lexend",sans-serif;font-size:18px;color:var(--white);font-weight:400}
.card p{position:absolute;top:256px;width:100%;text-align:center;font-size:14.5px;line-height:32px;color:var(--white)}
.card .go{position:absolute;left:50%;bottom:-18px;margin-left:-20px;width:40px;height:40px;border-radius:50%;background:var(--white);border:3px solid var(--ink);display:flex;align-items:center;justify-content:center}
.tab{position:absolute;top:2028px;font-size:17px;font-family:"Lexend",sans-serif;color:var(--text)}
.art-img{position:absolute;top:2752px;width:303px;height:231px;border-radius:0 0 60px 0}
.date{position:absolute;top:2970px;height:32px;padding:0 14px;background:var(--white);color:var(--blue);font-family:"Lexend",sans-serif;font-size:13px;font-weight:500;line-height:32px;clip-path:polygon(6px 0,100% 0,calc(100% - 6px) 100%,0 100%)}
.art-text{position:absolute;top:3012px;width:310px;font-size:15.5px;line-height:34px;color:var(--white)}
.foot-h{font-family:"Lexend",sans-serif;font-size:21px;color:var(--blue)}
.foot-link{position:absolute;font-size:13px;font-family:"Lexend",sans-serif;color:var(--ink)}
.foot-link::before{content:"";position:absolute;left:-24px;top:6px;width:6px;height:6px;border-radius:50%;background:var(--blue)}
.contact-ico{position:absolute;left:849px;width:34px;height:34px;border-radius:50%;background:var(--blue);display:flex;align-items:center;justify-content:center}
.contact-txt{position:absolute;left:901px;font-size:13px;font-family:"Lexend",sans-serif;color:var(--ink);line-height:26px}
</style>
</head>
<body>

<div class="photo" role="img" aria-label="Industrial pipework room tinted in blue" style="left:0;top:95px;width:1200px;height:530px;background:linear-gradient(120deg,#0f6aa3 0%,#155f91 45%,#0e527f 100%)"></div>
<svg class="abs" style="left:0;top:480px" width="1200" height="180" viewBox="0 0 1200 180">
  <polygon points="0,20 560,75 0,95" fill="#1b86c4"/>
  <polygon points="0,95 560,75 1200,110 1200,180 0,180" fill="#fff"/>
  <polygon points="560,75 1200,72 1200,145" fill="#000"/>
</svg>
<div class="photo" role="img" aria-label="Smiling plumber in hard hat and overalls with arms crossed" style="left:105px;top:130px;width:272px;height:402px;border-radius:110px 110px 0 0;background:linear-gradient(180deg,#c69a3f 0%,#5b4a3c 40%,#3b3d42 100%)"></div>
<div class="abs" style="left:571px;top:539px;width:40px;height:40px;border-radius:50%;background:#fff;border:1.5px solid var(--blue);display:flex;align-items:center;justify-content:center">
  <svg width="14" height="20" viewBox="0 0 14 20"><path d="M7 1v17M1 12l6 6 6-6" fill="none" stroke="#0b5b8e" stroke-width="1.8"/></svg>
</div>

<div class="abs call">
  <svg width="14" height="14" viewBox="0 0 24 24"><path d="M6.6 10.8c1.4 2.8 3.8 5.1 6.6 6.6l2.2-2.2c.3-.3.7-.4 1-.2 1.1.4 2.3.6 3.6.6.6 0 1 .4 1 1V20c0 .6-.4 1-1 1C10.6 21 3 13.4 3 4c0-.6.4-1 1-1h3.5c.6 0 1 .4 1 1 0 1.3.2 2.5.6 3.6.1.3 0 .7-.2 1L6.6 10.8z" fill="#0b5b8e"/></svg>
  <span>CALL US NOW : +1 555 014 2290</span>
</div>
<div class="btn" style="left:920px;top:25px;width:168px;height:30px;background:var(--blue-dark);color:#fff;font-size:12.5px">CHECK AVAILABILITY</div>
<div class="abs nav-band"></div>
<nav class="nav">
  <a class="active" style="left:134px">HOME</a>
  <a style="left:211px">RESIDENTIAL</a>
  <a style="left:316px">COMMERCIAL</a>
  <a style="left:428px">ABOUT</a>
  <a style="left:708px">BLOGS</a>
  <a style="left:778px">SCHEDULE SERVICE</a>
  <a style="left:928px">CONTACT US</a>
</nav>
<div class="abs logo-disc"></div>
<div class="abs logo-name" style="left:527px;top:58px;width:146px;font-size:17px;line-height:20px">KT<br>PLUMBLINE</div>

<h1 class="abs hero-title">EXPERT PLUMBING SOLUTIONS<br>IN CALIFORNIA</h1>
<p class="abs hero-text">Lorem ipsum dolor sit amet, consectetur adipiscing elit, sed do eiusmod tempor incididunt ut labore et dolore magna aliqua enim ad minim veniam quis nostrud exercitation</p>
<div class="btn btn-white" style="left:545px;top:443px;width:178px;height:35px">GET STARTED NOW</div>

<h2 class="abs sec-title" style="left:112px;top:638px">ABOUT <span class="accent">KT PLUMBLINE</span>
  <svg width="30" height="18" viewBox="0 0 30 18"><path d="M0 1h30M0 6h22M0 11h16M0 16h10" stroke="#0b5b8e" stroke-width="2"/></svg></h2>
<div class="abs para" style="left:112px;top:692px;width:460px">
  <p>Lorem ipsum dolor sit amet, consectetur adipiscing elit, sed do eiusmod tempor incididunt ut labore et dolore magna aliqua. Ut enim ad minim veniam, quis nostrud exercitation ullamco laboris nisi ut aliquip ex ea commodo consequat. Duis aute irure dolor in reprehenderit in voluptate velit esse cillum dolore eu fugiat nulla pariatur.</p>
  <p style="margin-top:8px">Lorem ipsum dolor sit amet, consectetur adipiscing elit, sed do eiusmod tempor incididunt ut labore et dolore magna aliquat enim ad minim veniam</p>
</div>
<div class="btn btn-blue" style="left:112px;top:1042px;width:135px;height:35px">LEARN MORE</div>
<div class="photo" role="img" aria-label="Plumber in blue cap repairing pipes under a sink" style="left:609px;top:672px;width:481px;height:382px;border-radius:0 0 0 90px;background:linear-gradient(135deg,#dfe6ee 0%,#3d6fb3 45%,#2a4f86 75%,#c9cfd6 100%)"></div>
<div class="abs" style="left:826px;top:841px;width:50px;height:50px;border-radius:50%;background:var(--blue);border:3px solid #fff;display:flex;align-items:center;justify-content:center">
  <svg width="16" height="18" viewBox="0 0 16 18"><path d="M2 1l13 8-13 8z" fill="#fff"/></svg>
</div>

<svg class="abs" style="left:0;top:1140px" width="1200" height="650" viewBox="0 0 1200 650">
  <polygon points="0,5 700,15 1200,0 1200,640 500,600 0,640" fill="#0b5b8e"/>
  <polygon points="700,15 1200,0 1200,32" fill="#000"/>
  <polygon points="0,610 500,602 0,640" fill="#000"/>
</svg>
<h2 class="abs sec-title" style="left:0;width:1200px;top:1205px;justify-content:center;color:#fff">OUR SERVICES
  <svg width="30" height="18" viewBox="0 0 30 18"><path d="M0 1h30M0 6h22M0 11h16M0 16h10" stroke="#fff" stroke-width="2"/></svg></h2>

<div class="card" style="left:115px">
  <div class="img" role="img" aria-label="Plumber fixing a bathroom radiator" style="background:linear-gradient(135deg,#e9e3dc,#9bb4c6 60%,#6d7f8c)"></div>
  <h3>RESIDENTIAL PLUMBING</h3>
  <p>Lorem ipsum dolor sit amet,<br>consectetur adipiscing elit, sed</p>
  <div class="go"><svg width="12" height="14" viewBox="0 0 12 14"><path d="M3 1l6 6-6 6" fill="none" stroke="#111" stroke-width="2.4"/></svg></div>
</div>
<div class="card" style="left:450px">
  <div class="img" role="img" aria-label="Technician in hi-vis vest inspecting industrial pipes" style="background:linear-gradient(135deg,#8f8b82,#c8b03a 45%,#5e5a53)"></div>
  <h3>COMMERCIAL PLUMBING</h3>
  <p>Lorem ipsum dolor sit amet,<br>consectetur adipiscing elit, sed</p>
  <div class="go"><svg width="12" height="14" viewBox="0 0 12 14"><path d="M3 1l6 6-6 6" fill="none" stroke="#111" stroke-width="2.4"/></svg></div>
</div>
<div class="card" style="left:785px">
  <div class="img" role="img" aria-label="Emergency responder inside a service vehicle" style="background:linear-gradient(135deg,#c9d3dc,#57605a 50%,#2e3130)"></div>
  <h3>EMERGENCY SERVICES</h3>
  <p>Lorem ipsum dolor sit amet,<br>consectetur adipiscing elit, sed</p>
  <div class="go"><svg width="12" height="14" viewBox="0 0 12 14"><path d="M3 1l6 6-6 6" fill="none" stroke="#111" stroke-width="2.4"/></svg></div>
</div>
<div class="btn btn-white" style="left:501px;top:1688px;width:197px;height:36px">VIEW MORE SERVICES</div>

<h2 class="abs sec-title" style="left:0;width:1200px;top:1842px;justify-content:center;color:var(--ink)">WHY <span class="accent">CHOOSE US</span>
  <svg width="30" height="18" viewBox="0 0 30 18"><path d="M0 1h30M0 6h22M0 11h16M0 16h10" stroke="#0b5b8e" stroke-width="2"/></svg></h2>
<svg class="abs" style="left:258px;top:1928px" width="66" height="72" viewBox="0 0 66 72" fill="none" stroke="#0b5b8e" stroke-width="2">
  <rect x="14" y="2" width="44" height="56"/><path d="M24 12h10v8H24zM40 14h12M40 20h12M24 30h28M24 38h28M30 46h22"/>
  <circle cx="14" cy="54" r="10" stroke="#222"/><path d="M8 62l-2 8 8-4 8 4-2-8" stroke="#222"/>
</svg>
<svg class="abs" style="left:560px;top:1924px" width="76" height="76" viewBox="0 0 76 76" fill="none" stroke="#222" stroke-width="2">
  <circle cx="38" cy="38" r="34"/><circle cx="38" cy="38" r="27"/>
  <text x="38" y="44" text-anchor="middle" font-family="Lexend,sans-serif" font-size="17" fill="#222" stroke="none">24/7</text>
</svg>
<svg class="abs" style="left:874px;top:1926px" width="70" height="74" viewBox="0 0 70 74" fill="none" stroke="#222" stroke-width="2">
  <path d="M35 3l3 7 7 .5-5.5 4.5 2 7-6.5-4-6.5 4 2-7L25 10.5l7-.5z"/>
  <path d="M12 10l2 5 5 .3-4 3 1.5 5-4.5-3-4.5 3 1.5-5-4-3 5-.3z"/>
  <path d="M58 10l2 5 5 .3-4 3 1.5 5-4.5-3-4.5 3 1.5-5-4-3 5-.3z"/>
  <rect x="4" y="42" width="12" height="28"/><path d="M16 46l10-10 4-10c4 0 6 4 4 10l-2 6h16c4 0 4 6 0 6 4 0 4 6 0 6 4 0 4 6 0 6 3 0 3 6-1 6H16"/>
</svg>
<div class="abs" style="left:162px;top:2015px;width:876px;height:3px;background:#e6e6e6"></div>
<div class="abs" style="left:162px;top:2014px;width:268px;height:4px;background:var(--blue)"></div>
<div class="tab" style="left:169px;color:var(--blue)">LICENSED PROFESSIONALS</div>
<div class="tab" style="left:516px">24/7 AVAILABILITY</div>
<div class="tab" style="left:787px">SATISFACTION GUARANTEE</div>

<div class="photo" role="img" aria-label="Plumber adjusting pipes beneath a sink with a screwdriver" style="left:112px;top:2110px;width:461px;height:407px;border-radius:0 0 80px 0;background:linear-gradient(120deg,#b6bcc2 0%,#e9ecef 40%,#7b6555 70%,#dcdfe2 100%)"></div>
<h3 class="abs sec-title" style="left:654px;top:2104px;font-size:22px;color:var(--blue)">LICENSED PROFESSIONALS
  <svg width="28" height="16" viewBox="0 0 30 18"><path d="M0 1h30M0 6h22M0 11h16M0 16h10" stroke="#0b5b8e" stroke-width="2"/></svg></h3>
<div class="abs para" style="left:654px;top:2151px;width:460px">
  <p>Lorem ipsum dolor sit amet, consectetur adipiscing elit, sed do eiusmod tempor incididunt ut labore et dolore magna aliquat enim ad minim veniam</p>
  <p style="margin-top:8px">Lorem ipsum dolor sit amet, consectetur adipiscing elit, sed do eiusmod tempor incididunt ut labore et dolore magna aliquat enim ad minim veniam quis nostrud exercitation ullamco laboris nisi ut aliquip ex ea commodo consequat.</p>
</div>
<div class="btn btn-blue" style="left:654px;top:2466px;width:135px;height:35px">LEARN MORE</div>

<svg class="abs" style="left:0;top:2595px" width="1200" height="660" viewBox="0 0 1200 660">
  <polygon points="0,0 600,18 1200,25 1200,620 700,640 0,648" fill="#0b5b8e"/>
  <polygon points="0,0 600,18 0,32" fill="#000"/>
  <polygon points="700,640 1200,620 1200,652" fill="#000"/>
</svg>
<h2 class="abs sec-title" style="left:0;width:1200px;top:2669px;justify-content:center;color:#fff">LATEST ARTICLES
  <svg width="30" height="18" viewBox="0 0 30 18"><path d="M0 1h30M0 6h22M0 11h16M0 16h10" stroke="#fff" stroke-width="2"/></svg></h2>

<div class="art-img" role="img" aria-label="Gloved hands tightening a chrome sink trap" style="left:114px;background:linear-gradient(135deg,#f1f1f1,#c9cdd1 50%,#2a3fb0)"></div>
<div class="art-img" role="img" aria-label="Plumber in white helmet working on a shower wall" style="left:449px;background:linear-gradient(135deg,#8e8c89,#d8d6d2 55%,#6c6a66)"></div>
<div class="art-img" role="img" aria-label="Hands fitting a water meter on pipework" style="left:784px;background:linear-gradient(135deg,#3a5fa2,#7e8d9b 50%,#4a3a33)"></div>
<div class="date" style="left:105px">05TH APRIL 2024</div>
<div class="date" style="left:440px">15TH JUNE 2024</div>
<div class="date" style="left:774px">06TH APRIL 2024</div>
<p class="art-text" style="left:114px">Lorem ipsum dolor sit amet, consectetur adipiscing elit, sed do eiusmod tempor incididunt</p>
<p class="art-text" style="left:449px">Lorem ipsum dolor sit amet, consectetur adipiscing elit, sed do eiusmod tempor incididunt</p>
<p class="art-text" style="left:784px">Lorem ipsum dolor sit amet, consectetur adipiscing elit, sed do eiusmod tempor incididunt</p>
<div class="btn btn-white" style="left:501px;top:3146px;width:197px;height:36px">VIEW MORE ARTICLES</div>

<div class="abs" style="left:112px;top:3360px;display:flex;align-items:center;gap:10px">
  <div style="width:22px;height:22px;border-radius:50%;background:var(--blue)"></div>
  <div class="logo-name" style="font-size:22px">KT PLUMBLINE</div>
</div>
<div class="abs" style="left:340px;top:3304px;width:1px;height:202px;background:var(--line)"></div>
<div class="abs" style="left:785px;top:3304px;width:1px;height:202px;background:var(--line)"></div>

<div class="abs foot-h" style="left:404px;top:3300px">QUICK LINKS</div>
<div class="foot-link" style="left:429px;top:3361px">HOME</div>
<div class="foot-link" style="left:429px;top:3395px">RESIDENTIAL</div>
<div class="foot-link" style="left:429px;top:3429px">COMMERCIAL</div>
<div class="foot-link" style="left:429px;top:3463px">ABOUT</div>
<div class="foot-link" style="left:614px;top:3361px">BLOGS</div>
<div class="foot-link" style="left:614px;top:3395px">SCHEDULE SERVICE</div>
<div class="foot-link" style="left:614px;top:3429px">CONTACT US</div>

<div class="abs foot-h" style="left:849px;top:3300px">CONTACT US</div>
<div class="contact-ico" style="top:3353px"><svg width="14" height="14" viewBox="0 0 24 24"><path d="M6.6 10.8c1.4 2.8 3.8 5.1 6.6 6.6l2.2-2.2c.3-.3.7-.4 1-.2 1.1.4 2.3.6 3.6.6.6 0 1 .4 1 1V20c0 .6-.4 1-1 1C10.6 21 3 13.4 3 4c0-.6.4-1 1-1h3.5c.6 0 1 .4 1 1 0 1.3.2 2.5.6 3.6.1.3 0 .7-.2 1L6.6 10.8z" fill="#fff"/></svg></div>
<div class="contact-txt" style="top:3357px">+1 555 014 2290</div>
<div class="contact-ico" style="top:3403px"><svg width="16" height="12" viewBox="0 0 16 12"><rect x="1" y="1" width="14" height="10" fill="none" stroke="#fff" stroke-width="1.5"/><path d="M1 1l7 6 7-6" fill="none" stroke="#fff" stroke-width="1.5"/></svg></div>
<div class="contact-txt" style="top:3407px">HELLO@KTPLUMBLINE.EXAMPLE</div>
<div class="contact-ico" style="top:3453px"><svg width="12" height="16" viewBox="0 0 12 16"><path d="M6 15S1 9 1 6a5 5 0 0110 0c0 3-5 9-5 9z" fill="none" stroke="#fff" stroke-width="1.5"/><circle cx="6" cy="6" r="1.8" fill="#fff"/></svg></div>
<div class="contact-txt" style="top:3457px">1234 VALVE CREST WAY<br>FRESNO, CA 93701</div>

<div class="abs" style="left:110px;top:3548px;width:980px;height:1px;background:var(--line)"></div>
<p class="abs" style="left:0;width:1200px;top:3565px;text-align:center;font-family:'Lexend',sans-serif;font-size:12.5px;color:var(--ink)">COPYRIGHTS 2024 <span style="color:var(--blue)">KT PLUMBLINE</span>. ALL RIGHTS RESERVED.</p>

</body>
</html>
```